New flyer design for construction company marketing and description of services.

I want to have a flyer design that my techs will carry to deliver after job completion or for marketing purposes, to explain what services we provide, we offer General construction services.

Brellor Homecraft Sevices originated from a family-owned and operated contractor business, performing home renovation, addition, and construction work in the NYC area since 2004.

Today, we specialize in reliable and affordable Construction services for residential and commercial clients In 2014, we expanded to northern New Jersey. In 2016, we brought quality home improvement and repair services to new Bucks County, PA, and nearby New Jersey areas.
We offer carpentry, electrical, plumbing, renovation, remodel, cleaning services and landscaping.
I would like to have a section for home rental maintenance.

Target Market(s)

Homeowners, rental properties, real state and Senior citizen

Industry/Entity Type

Construction Company

Colors

Designer to choose colors to be used in the design.

Requirements
Must have
• A special design that will attract 55 + clients maybe a logo version that will be more attractive to seniors. I would updated the briefing with design and previous pictures, but we have all available in our social media instagram and facebook:
• https://www.pictogram.example/brellorhomecraft/?hl=en
• https://www.friendsbook.example/brellorhome/
Nice to have
• New design ideas and layouts.

```html
<!DOCTYPE html>
<html lang="en">
<head>
<meta charset="utf-8">
<title>Brellor Homecraft Sevices – Flyer</title>
<link href="https://fonts.googleapis.com/css2?family=Lato:wght@400;700;900&family=Montserrat:wght@700;800&family=Open+Sans:wght@700;800&display=swap" rel="stylesheet">
<style>
  :root {
    --backdrop: #3a3a3a;
    --red: #f00000;
    --deep-red: #c8140f;
    --ink: #151515;
    --paper: #ffffff;
    --mist: #eeeeee;
    --frame: #d9d9d9;
    --edge: #4a4a4a;
  }
  * { margin: 0; padding: 0; box-sizing: border-box; }
  html, body {
    width: 1200px; height: 1200px; overflow: hidden;
    background: var(--backdrop);
  }
  .flyer {
    position: absolute; left: 290px; top: 153px;
    width: 773px; height: 1159px;
    transform: scale(0.8); transform-origin: 0 0;
    background: linear-gradient(180deg, var(--paper) 0%, var(--mist) 60%, #e4e4e4 100%);
    overflow: hidden;
    font-family: "Lato", sans-serif; color: var(--ink);
  }
  .flyer-shapes { position: absolute; inset: 0; }
  .abs { position: absolute; }

  .brand { left: 18px; top: 82px; display: flex; align-items: center; gap: 12px; }
  .brand-dot { width: 56px; height: 56px; border-radius: 50%; background: var(--red); }
  .brand-name { font-family: "Montserrat", sans-serif; font-weight: 800; font-size: 44px; line-height: 1; color: var(--ink); }
  .brand-line { font-family: "Montserrat", sans-serif; font-weight: 800; font-size: 9px; letter-spacing: 3px; color: var(--ink); margin-top: 4px; }

  .title {
    left: 12px; top: 258px;
    font-family: "Montserrat", sans-serif; font-weight: 800; font-size: 31px; line-height: 40px;
    color: var(--deep-red); letter-spacing: 0.5px;
  }
  .rule { height: 4px; background: var(--ink); }

  .lead { left: 12px; top: 352px; font-weight: 700; font-size: 21px; line-height: 30px; letter-spacing: -0.3px; }

  .bullets { list-style: none; font-size: 21px; }
  .bullets li { position: relative; padding-left: 22px; height: 38px; line-height: 26px; }
  .bullets li::before {
    content: ""; position: absolute; left: 0; top: 9px;
    width: 9px; height: 9px; border-radius: 50%; background: var(--ink);
  }
  .bullets.tight li { height: 32px; }

  .section-head { font-family: "Montserrat", sans-serif; font-weight: 800; font-size: 20px; letter-spacing: 0.5px; }
  .about-head { font-family: "Montserrat", sans-serif; font-weight: 800; font-size: 31px; }
  .about-head .accent { color: var(--deep-red); }
  .about-text { left: 15px; top: 782px; width: 390px; font-size: 16px; line-height: 19.5px; letter-spacing: -0.2px; }

  .slogan {
    right: 13px; top: 748px; text-align: right;
    font-family: "Open Sans", sans-serif; font-weight: 800; color: var(--paper);
    font-size: 60px; line-height: 64px; letter-spacing: -1.5px;
  }
  .contact {
    right: 28px; display: flex; align-items: center; gap: 16px;
    font-family: "Open Sans", sans-serif; font-weight: 800; color: var(--paper);
    font-size: 27px; letter-spacing: 0.3px;
  }
</style>
</head>
<body>
<main class="flyer">
  <svg class="flyer-shapes" viewBox="0 0 773 1159" width="773" height="1159">
    <defs>
      <linearGradient id="crewTone" x1="0" y1="0" x2="1" y2="1">
        <stop offset="0" stop-color="#c9ccce"/>
        <stop offset="0.45" stop-color="#9fb2c9"/>
        <stop offset="0.75" stop-color="#5f7fae"/>
        <stop offset="1" stop-color="#c2383a"/>
      </linearGradient>
      <linearGradient id="windowTone" x1="0" y1="0" x2="1" y2="1">
        <stop offset="0" stop-color="#b7c9c4"/>
        <stop offset="0.55" stop-color="#8aa1a8"/>
        <stop offset="1" stop-color="#6f9a4a"/>
      </linearGradient>
      <linearGradient id="panelTone" x1="0" y1="0" x2="1" y2="1">
        <stop offset="0" stop-color="#e7e7e3"/>
        <stop offset="0.5" stop-color="#c9c3a0"/>
        <stop offset="1" stop-color="#8f9a8f"/>
      </linearGradient>
    </defs>
    <polygon points="152,0 773,0 773,404 590,545" fill="url(#crewTone)" role="img" aria-label="Photo of two construction workers in hard hats reviewing plans"/>
    <polygon points="0,191 327,191 345,209 0,209" fill="var(--red)"/>
    <polygon points="773,404 773,1159 0,1159 0,859 150,1000 297,949" fill="var(--red)"/>
    <polygon points="773,394 773,404 590,548 582,540" fill="var(--edge)"/>
    <polygon points="0,842 90,925 78,937 0,866" fill="var(--edge)"/>
    <g transform="translate(569 637) rotate(45)">
      <rect x="-100" y="-100" width="200" height="200" rx="52" fill="var(--frame)"/>
      <rect x="-92" y="-92" width="184" height="184" rx="46" fill="url(#windowTone)" role="img" aria-label="Photo of a worker cleaning a window beside garden plants"/>
    </g>
    <g transform="translate(175 999) rotate(45)">
      <rect x="-100" y="-100" width="200" height="200" rx="52" fill="var(--frame)"/>
      <rect x="-92" y="-92" width="184" height="184" rx="46" fill="url(#panelTone)" role="img" aria-label="Photo of a hand testing wiring in an electrical panel"/>
    </g>
  </svg>

  <div class="abs brand">
    <span class="brand-dot"></span>
    <div>
      <div class="brand-name">Brellor</div>
      <div class="brand-line">HOMECRAFT SERVICES</div>
    </div>
  </div>

  <h1 class="abs title">BRELLOR HOMECRAFT<br>SEVICES</h1>
  <div class="abs rule" style="left:0;top:336px;width:150px"></div>

  <p class="abs lead">CALL THE PROS, NOT THE CONS.<br>We do It all, Large &amp; small :</p>

  <ul class="abs bullets" style="left:38px;top:424px">
    <li>Small Repairs</li>
    <li>Remodelling</li>
    <li>General Contractiong</li>
  </ul>

  <h2 class="abs section-head" style="left:12px;top:545px">SERVICES :</h2>
  <div class="abs rule" style="left:0;top:572px;width:122px;height:3px"></div>

  <ul class="abs bullets tight" style="left:38px;top:584px">
    <li>Carpentry</li>
    <li>Plumbing</li>
    <li>Remodel</li>
    <li>Landscapes</li>
  </ul>
  <ul class="abs bullets tight" style="left:213px;top:584px">
    <li>Electrical</li>
    <li>Renovation</li>
    <li>Cleaning Services</li>
    <li>Thermal Inspection</li>
  </ul>

  <h2 class="abs about-head" style="left:14px;top:732px"><span class="accent">ABOUT</span> US</h2>
  <div class="abs rule" style="left:0;top:772px;width:162px;height:3px"></div>
  <p class="abs about-text">BRELLOR HOMECRAFT SEVICES based in Langhorne , PA Serving Bucks County, Montgomery County , Mercer County, Burlington County</p>

  <p class="abs slogan">A<br>BETTER WAY<br>TO GET<br>TASKS DONE</p>

  <div class="abs contact" style="top:1058px">
    <span>www.brellor.example</span>
    <svg width="34" height="34" viewBox="0 0 34 34" aria-hidden="true">
      <circle cx="17" cy="17" r="15" fill="none" stroke="var(--paper)" stroke-width="3"/>
      <ellipse cx="17" cy="17" rx="6" ry="15" fill="none" stroke="var(--paper)" stroke-width="2.5"/>
      <line x1="2" y1="17" x2="32" y2="17" stroke="var(--paper)" stroke-width="2.5"/>
    </svg>
  </div>
  <div class="abs contact" style="top:1108px">
    <span>(555) 014-2290</span>
    <svg width="34" height="34" viewBox="0 0 24 24" aria-hidden="true">
      <path fill="var(--paper)" d="M6.6 10.8a15.1 15.1 0 0 0 6.6 6.6l2.2-2.2c.3-.3.7-.4 1-.2 1.1.4 2.3.6 3.6.6.6 0 1 .4 1 1V20c0 .6-.4 1-1 1C10.6 21 3 13.4 3 4c0-.6.4-1 1-1h3.5c.6 0 1 .4 1 1 0 1.3.2 2.5.6 3.6.1.3 0 .7-.2 1z"/>
    </svg>
  </div>
</main>
</body>
</html>
```